Business Card design for an Oilfield Service Co
Wrenmoor Oilfield
Modern
Clara Totsby
Sales
Tensley Hollow Road Port Washington, OH 41926
clara.totsby@wrenmoorgroup.example
Light Towers Balloon Lights Generators Flameless Heaters Glycol (Ground) Heaters Man Lifts Fork Lifts Back Hoes Skid Steers Pumps Air Compressors Safety Trailers/Showers Trash Trailers/Porta Potty Guard Shack Rental Super Vac Trucks Pressure Washing Roustabout Tank/Pit Cleaning Rig Washing Hot Shot Industrial Coatings Absorbents Mobile Fueling Service 24 Hour Service Calls

```html
<!DOCTYPE html>
<html lang="en">
<head>
<meta charset="utf-8">
<title>Wrenmoor Oilfield – Business Card</title>
<link href="https://fonts.googleapis.com/css2?family=Oswald:wght@500&family=Roboto:wght@400&display=swap" rel="stylesheet">
<style>
  :root{
    --bg:#c9c9c9;
    --card:#f7f7f7;
    --ink:#2b2b2b;
    --muted:#555555;
    --accent:#e4e01f;
    --rule:#2b2b2b;
  }
  *{margin:0;padding:0;box-sizing:border-box}
  html,body{width:1200px;height:946px;overflow:hidden}
  body{
    background:var(--bg);
    font-family:'Roboto',Arial,sans-serif;
    color:var(--ink);
    position:relative;
  }
  .card{
    position:absolute;
    left:250px;
    width:700px;
    height:400px;
    background:var(--card);
    border-radius:22px;
    box-shadow:0 6px 18px rgba(0,0,0,.18);
  }
  .card--back{top:48px}
  .card--front{top:498px}

  .brand{
    position:absolute;
    display:flex;
    align-items:center;
    gap:10px;
    font-family:'Oswald',Arial,sans-serif;
    font-weight:500;
    font-size:30px;
    letter-spacing:1px;
    text-transform:uppercase;
    color:var(--ink);
    white-space:nowrap;
  }
  .brand__dot{
    width:22px;height:22px;border-radius:50%;
    background:var(--accent);
    flex:none;
  }
  .card--back .brand{left:50%;top:50%;transform:translate(-50%,-50%)}
  .card--front .brand{left:36px;top:50%;transform:translateY(-50%);font-size:24px}
  .card--front .brand__dot{width:18px;height:18px}

  .social{
    position:absolute;
    right:40px;bottom:30px;
    display:flex;gap:26px;
    font-size:15px;color:var(--muted);
  }
  .social__item{display:flex;align-items:center;gap:8px}
  .social__mark{width:18px;height:18px;background:var(--ink);border-radius:2px}

  .details{
    position:absolute;
    left:300px;top:46px;
    display:flex;flex-direction:column;gap:28px;
  }
  .block{
    display:flex;align-items:center;gap:18px;
  }
  .block__icon{width:32px;height:32px;flex:none}
  .block__text{
    border-left:3px solid var(--rule);
    padding-left:14px;
    line-height:1.4;
    font-size:16px;
    color:var(--muted);
    white-space:nowrap;
  }
  .person__name{
    font-family:'Oswald',Arial,sans-serif;
    font-weight:500;
    font-size:28px;
    letter-spacing:1.5px;
    text-transform:uppercase;
    color:var(--ink);
    line-height:1.15;
  }
  .person__role{font-size:16px;color:var(--muted)}
  .block--person .block__text{border-left-width:4px}
</style>
</head>
<body>

  <section class="card card--back" aria-label="Business card, back">
    <div class="brand"><span class="brand__dot"></span>Wrenmoor Oilfield</div>
    <div class="social">
      <span class="social__item"><span class="social__mark"></span>/wrenmoorfield</span>
      <span class="social__item"><span class="social__mark"></span>@wrenmoorfield</span>
    </div>
  </section>

  <section class="card card--front" aria-label="Business card, front">
    <div class="brand"><span class="brand__dot"></span>Wrenmoor Oilfield</div>

    <div class="details">
      <div class="block block--person">
        <svg class="block__icon" viewBox="0 0 34 34" aria-hidden="true">
          <circle cx="17" cy="11" r="7" fill="var(--accent)"/>
          <path d="M4 32c0-8 6-12 13-12s13 4 13 12z" fill="var(--accent)"/>
        </svg>
        <div class="block__text">
          <div class="person__name">Clara Totsby</div>
          <div class="person__role">Sales</div>
        </div>
      </div>

      <div class="block">
        <svg class="block__icon" viewBox="0 0 34 34" aria-hidden="true">
          <path d="M17 2a11 11 0 0 0-11 11c0 8 11 19 11 19s11-11 11-19A11 11 0 0 0 17 2z" fill="var(--accent)"/>
          <circle cx="17" cy="13" r="4.5" fill="var(--card)"/>
        </svg>
        <div class="block__text">
          Tensley Hollow Road<br>Port Washington, OH 41926
        </div>
      </div>

      <div class="block">
        <svg class="block__icon" viewBox="0 0 34 34" aria-hidden="true">
          <g fill="none" stroke="var(--accent)" stroke-width="2.2">
            <circle cx="17" cy="17" r="14"/>
            <ellipse cx="17" cy="17" rx="6" ry="14"/>
            <line x1="3" y1="17" x2="31" y2="17"/>
            <path d="M6 9h22M6 25h22"/>
          </g>
        </svg>
        <div class="block__text">
          012 555 0142<br>clara.totsby@wrenmoorgroup.example<br>www.wrenmoorgroup.example
        </div>
      </div>
    </div>
  </section>

</body>
</html>
```